Harwick Vitality Circle needs a stand-up Banner Deadline Oct 2

We need a stand-up banner design for Harwick College Vitality Circle. Our aim is to spread awareness of emerging ideas and technologies in various scientific fields with a particular emphasis on geroscience (hence the name), but not restricted to it. We organise various projects, talks by prominent scientists and conferences.

We urgently need a design for a vertical roll up banner to be used in our events (beside the stage) and an upcoming freshers' fair.

I'm attaching our logo (you can separate the circular logo from the "Vitality Circle" text if you like) and a picture of Cambridge that you could use if needed. We are open to use of stock photos.

Size: 800 x 2000

Target Market(s)

Harwick College Students

Industry/Entity Type

University

Requirements
Must have
• -Logo
• -Either "Vitality Circle" or "Harwick College Vitality Circle" name
• -Text "Spreading awareness of emerging ideas and technologies"
• -Friendspace page https://www.facebook.com/HarCVCirc/
• -Email hcvitality@mailnook.net
Nice to have
• -Some of the colours I envision for the banner are: green, blue, white
• -Scientific and/or innovative feeling

```html
<!DOCTYPE html>
<html lang="en">
<head>
<meta charset="utf-8">
<title>Vitality Circle – Roll-up Banner</title>
<link rel="stylesheet" href="https://fonts.googleapis.com/css2?family=Cinzel:wght@500&family=Open+Sans:wght@400;700;800&display=swap">
<style>
  :root {
    --canvas-bg: #e6e6e6;
    --white: #ffffff;
    --ink: #141414;
    --green: #1f9a4a;
    --green-light: #8cc63f;
    --blue: #1565c0;
    --sky-top: #8fb8dc;
    --sky-low: #d9e6ee;
    --stone: #c9a95e;
    --lawn: #4f8a2e;
    --water: #6f8a8c;
  }
  * { margin: 0; padding: 0; box-sizing: border-box; }
  html, body {
    width: 1200px;
    height: 1200px;
    overflow: hidden;
    background: var(--canvas-bg);
  }
  .canvas {
    position: relative;
    width: 1200px;
    height: 1200px;
  }
  .banner {
    position: absolute;
    left: 382px;
    top: 40px;
    width: 436px;
    height: 1120px;
    background: var(--white);
    overflow: hidden;
    font-family: "Open Sans", Arial, sans-serif;
    box-shadow: 0 6px 24px rgba(0,0,0,0.18);
  }
  .banner-shapes {
    position: absolute;
    inset: 0;
    width: 100%;
    height: 100%;
  }
  .brand {
    position: absolute;
    top: 80px;
    left: 0;
    width: 100%;
    display: flex;
    justify-content: center;
    align-items: center;
    gap: 16px;
  }
  .brand-dot {
    width: 50px;
    height: 50px;
    border-radius: 50%;
    background: var(--green);
  }
  .brand-name {
    font-family: "Cinzel", Georgia, serif;
    font-weight: 500;
    font-size: 25px;
    letter-spacing: 1.5px;
    color: var(--green);
  }
  .headline {
    position: absolute;
    left: 0;
    width: 100%;
    text-align: center;
    line-height: 1;
    white-space: nowrap;
  }
  .headline-lead {
    font-weight: 700;
    font-size: 39px;
    color: var(--ink);
  }
  .headline-lead.first { top: 180px; }
  .headline-lead.second { top: 226px; }
  .headline-key {
    top: 276px;
    font-weight: 800;
    font-size: 58px;
    color: var(--green);
  }
  .headline-sub {
    font-weight: 800;
    font-size: 35px;
    color: var(--green);
  }
  .headline-sub.ideas { top: 344px; }
  .headline-sub.tech { top: 388px; }
  .headline-sub .plain {
    font-weight: 400;
    color: var(--ink);
  }
  .contact {
    position: absolute;
    left: 0;
    width: 100%;
    text-align: center;
    color: var(--white);
    white-space: nowrap;
    line-height: 1;
  }
  .contact-label { font-size: 16px; font-weight: 400; }
  .contact-label.social { top: 990px; }
  .contact-label.mail { top: 1056px; }
  .contact-link.social { top: 1012px; font-size: 19px; font-weight: 700; }
  .contact-link.mail { top: 1080px; font-size: 25px; font-weight: 700; }
</style>
</head>
<body>
<div class="canvas">
  <div class="banner">
    <svg class="banner-shapes" viewBox="0 0 322 828" preserveAspectRatio="none">
      <defs>
        <linearGradient id="scene-fill" x1="0" y1="0" x2="0" y2="1">
          <stop offset="0" stop-color="var(--sky-top)"/>
          <stop offset="0.35" stop-color="var(--sky-low)"/>
          <stop offset="0.5" stop-color="var(--stone)"/>
          <stop offset="0.66" stop-color="var(--lawn)"/>
          <stop offset="0.8" stop-color="var(--water)"/>
          <stop offset="1" stop-color="var(--stone)"/>
        </linearGradient>
      </defs>
      <polygon class="accent-blue" points="72,380 322,290 322,318" fill="var(--blue)"/>
      <polygon class="accent-green-left" points="0,360 92,382 0,414" fill="var(--green-light)"/>
      <g role="img" aria-label="Photograph of a historic college chapel and lawns reflected in a river">
        <polygon class="scene" points="0,405 322,335 322,628 0,708" fill="url(#scene-fill)"/>
      </g>
      <polygon class="accent-green-right" points="215,655 322,628 322,662" fill="var(--green-light)"/>
      <polygon class="footer-band" points="0,722 322,652 322,822 0,822" fill="var(--green)"/>
      <rect class="footer-line" x="0" y="822" width="322" height="6" fill="var(--blue)"/>
    </svg>

    <div class="brand">
      <span class="brand-dot"></span>
      <span class="brand-name">VITALITY CIRCLE</span>
    </div>

    <div class="headline headline-lead first">spreading</div>
    <div class="headline headline-lead second">awareness of</div>
    <div class="headline headline-key">EMERGING</div>
    <div class="headline headline-sub ideas">IDEAS <span class="plain">AND</span></div>
    <div class="headline headline-sub tech">TECHNOLOGIES</div>

    <div class="contact contact-label social">Follow us on Friendspace</div>
    <div class="contact contact-link social">www.friendspace.net/HarCVCirc/</div>
    <div class="contact contact-label mail">Mail us for any query</div>
    <div class="contact contact-link mail">hcvitality@mailnook.net</div>
  </div>
</div>
</body>
</html>
```